Law Firm Local Movie Theatre Screen Ad

Our law firm sponsor our local movie theater. In exchange for our sponsorship, they put up a visual advertisement for our law firm before the movie starts. We have an existing ad (see below) but it is a little dated and we want something fresh. I has to be basic because it only flashes on the screen for a few seconds (other ads scroll continuously). It also needs to have enough quality to be REALLY big on the screen without getting blurry. We have higher resolution photos of people if necessary.

Target Market(s)

People looking for a law firm

Industry/Entity Type

Law Firm

Requirements
Must have
• photo of building - so they connect our firm location with us (the theater is down the street).
• Must be 1920 x 1080 72dpi
Should not have
• Specific details about practice areas (i.e Personal Injury, etc)

```html
<!DOCTYPE html>
<html lang="en">
<head>
<meta charset="utf-8">
<title>Hollis Brennan – Theatre Screen Ad</title>
<link href="https://fonts.googleapis.com/css2?family=Questrial&family=Libre+Baskerville:ital,wght@1,400&display=swap" rel="stylesheet">
<style>
  :root {
    --bg: #f3f3f4;
    --ink: #1d1d1d;
    --taupe: #b9aaa5;
    --sketch-light: #e4e2df;
    --sketch-dark: #6f6a64;
  }
  html, body {
    margin: 0;
    padding: 0;
    width: 1200px;
    height: 675px;
    overflow: hidden;
    background: var(--bg);
  }
  .ad {
    position: relative;
    width: 1200px;
    height: 675px;
    background: var(--bg);
    color: var(--ink);
    font-family: "Questrial", "Helvetica Neue", Arial, sans-serif;
  }
  .firm-name {
    position: absolute;
    left: 42px;
    top: 46px;
    width: 1098px;
    height: 80px;
    margin: 0;
    display: flex;
    align-items: center;
    justify-content: center;
    font-family: "Questrial", Arial, sans-serif;
    font-weight: 400;
    font-size: 60px;
    letter-spacing: 0.2em;
    color: var(--ink);
    white-space: nowrap;
  }
  .tagline {
    position: absolute;
    right: 60px;
    top: 132px;
    margin: 0;
    font-family: "Libre Baskerville", Georgia, serif;
    font-style: italic;
    font-size: 38px;
    line-height: 1;
    color: var(--ink);
  }
  .year {
    position: absolute;
    left: 48px;
    top: 228px;
    margin: 0;
    font-size: 114px;
    line-height: 1;
    font-weight: 400;
  }
  .award {
    position: absolute;
    left: 48px;
    top: 340px;
    margin: 0;
    font-size: 70px;
    line-height: 70px;
    font-weight: 400;
  }
  .location-line {
    position: absolute;
    left: 44px;
    top: 572px;
    margin: 0;
    font-size: 52px;
    line-height: 1;
  }
  .building {
    position: absolute;
    left: 632px;
    top: 304px;
    width: 512px;
    height: 248px;
  }
</style>
</head>
<body>
  <main class="ad">
    <h1 class="firm-name">HOLLIS BRENNAN</h1>
    <p class="tagline">attorneys at law</p>

    <p class="year">2016</p>
    <p class="award">Best law firms<br>in America</p>

    <svg class="building" viewBox="0 0 512 248" role="img" aria-label="Sketch of the firm's two-storey corner office building with awnings and a street-corner lamp post">
      <defs>
        <linearGradient id="buildingTone" x1="0" y1="0" x2="0" y2="1">
          <stop offset="0" stop-color="var(--sketch-dark)" stop-opacity="0.55"/>
          <stop offset="0.3" stop-color="var(--sketch-light)"/>
          <stop offset="1" stop-color="var(--bg)"/>
        </linearGradient>
      </defs>
      <rect x="0" y="0" width="512" height="248" fill="url(#buildingTone)"/>
    </svg>

    <p class="location-line">Just around the corner</p>
  </main>
</body>
</html>
```